Business card design needed

I would like to show the combination of Handyman and Garden Service on my card.

There are two designs in my mind.

1.
A cartoon showing a smiling man in a good mute working in the garden on a sunny day, maybe sweating like crazy.
A belt full of tools with e.g. hammer, saw, tong and tape measure.
Pushing a lawnmower with one hand and trimming the hedge with the other at the same time. There could be also some tools in a basket attached to the handle at the lawnmower and maybe a chainsaw is hanging on the neck of the man.

I would love to have this picture later for my letter header too.

If this is not possible or to expensive

2.
the card could have several icons to show the different activities.

If you find any better words for the backside please feel free to use them.

Requirements
Must have
• Front:
The picture or the icons witch I described, company name, address, mobile number, email.

Back:

```html
<!DOCTYPE html>
<html lang="en">
<head>
<meta charset="utf-8">
<title>Dean's Handyman &amp; Garden Service – Business Card</title>
<link rel="stylesheet" href="https://fonts.googleapis.com/css2?family=Oswald:wght@600&family=Questrial&display=swap">
<style>
  :root {
    --card-bg: #ffffff;
    --brand-green: #55e33c;
    --lawn-green: #a4ec4c;
    --hedge-green: #3fb52a;
    --figure-tone: #e6d2b4;
    --mower-red: #e8332a;
    --shirt-orange: #d9761e;
  }
  html, body {
    margin: 0;
    padding: 0;
    width: 1200px;
    height: 693px;
    overflow: hidden;
    background: var(--card-bg);
  }
  .card {
    position: relative;
    width: 1200px;
    height: 693px;
    background: var(--card-bg);
    overflow: hidden;
  }
  .business-name {
    position: absolute;
    top: 74px;
    left: 0;
    width: 1200px;
    margin: 0;
    text-align: center;
    font-family: "Oswald", "Arial Narrow", sans-serif;
    font-weight: 600;
    font-size: 66px;
    line-height: 1;
    letter-spacing: 0.5px;
    color: var(--brand-green);
  }
  .email {
    position: absolute;
    top: 158px;
    left: 0;
    width: 1200px;
    margin: 0;
    text-align: center;
    font-family: "Questrial", "Century Gothic", sans-serif;
    font-size: 38px;
    line-height: 1;
    color: var(--brand-green);
  }
  .lawn-band {
    position: absolute;
    left: 23px;
    top: 600px;
    width: 1170px;
    height: 70px;
  }
  .mascot-art {
    position: absolute;
    left: 23px;
    top: 226px;
    width: 600px;
    height: 400px;
    border-radius: 6px;
    background:
      radial-gradient(ellipse at 12% 60%, var(--hedge-green) 0 28%, transparent 29%),
      radial-gradient(ellipse at 80% 80%, var(--mower-red) 0 14%, transparent 15%),
      radial-gradient(ellipse at 42% 45%, var(--shirt-orange) 0 12%, transparent 13%),
      linear-gradient(160deg, #f4ece0 0%, var(--figure-tone) 60%, #cfe9b4 100%);
  }
  .contact {
    position: absolute;
    right: 67px;
    top: 372px;
    margin: 0;
    text-align: right;
    font-family: "Oswald", "Arial Narrow", sans-serif;
    font-weight: 600;
    font-size: 52px;
    line-height: 67px;
    color: var(--brand-green);
    font-style: normal;
  }
  .contact span { display: block; }
</style>
</head>
<body>
  <main class="card">
    <h1 class="business-name">Dean’s Handyman &amp; Garden Service</h1>
    <p class="email">deanshandymangardenservice@mailbox.com</p>

    <svg class="lawn-band" viewBox="0 0 1170 70" aria-hidden="true">
      <rect x="0" y="10" width="1170" height="60" fill="var(--lawn-green)"/>
    </svg>

    <div class="mascot-art" role="img"
         aria-label="Cartoon of a sweating, smiling handyman in cap and tool belt trimming a hedge with one hand while pushing a red lawnmower with the other"></div>

    <address class="contact">
      <span>14 Wattle Close</span>
      <span>Brookfield, QLD&nbsp; 4870</span>
      <span>Mobile: 04 5550 1264</span>
    </address>
  </main>
</body>
</html>
```